professional business card design for technology company

We are a small technology consulting firm, specialising in consulting based around Cloud and Managed services. Our colour scheme is yellow, blue and white, as you can see in the logos. Although we are based in melbourne australia, due to the nature of our work, our clients can be located anywhere. We are looking for a clean, professional, positive look - similar to our company logo

Target Market(s)

small business

Industry/Entity Type

Business

Contact Information for Business Card

eye catching, designed to incorporate some level of raised printing. Must contain website address, phone number, name and job title

Requirements
Must have
• Logo (attached) - use of the same colour scheme

```html
<!DOCTYPE html>
<html lang="en">
<head>
<meta charset="utf-8">
<title>Nubiro – Business Card</title>
<link href="https://fonts.googleapis.com/css2?family=Open+Sans:wght@400;600;800&display=swap" rel="stylesheet">
<style>
  :root{
    --page:#8c8c8c;
    --paper:#ffffff;
    --ink:#3a3a3a;
    --band:#5f6062;
    --band-dark:#4d4e50;
    --accent:#2aa6e0;
    --sun:#f2c41b;
    --light:#ffffff;
    --faint:#7a7b7d;
  }
  *{margin:0;padding:0;box-sizing:border-box}
  html,body{width:1200px;height:772px;overflow:hidden}
  body{
    background:var(--page);
    font-family:"Open Sans",Arial,sans-serif;
    display:flex;align-items:center;justify-content:center;gap:40px;
  }
  .card{
    position:relative;width:540px;height:309px;overflow:hidden;
    border-radius:3px;box-shadow:0 6px 18px rgba(0,0,0,.25);
  }
  /* front */
  .card-front{background:var(--paper);color:var(--ink)}
  .card-front .swoosh{position:absolute;inset:0;width:100%;height:100%}
  .brand{
    position:absolute;left:34px;top:38px;display:flex;align-items:center;gap:12px;
  }
  .brand-mark{width:22px;height:22px;border-radius:50%;background:var(--accent)}
  .brand-name{font-weight:800;font-size:44px;line-height:1;color:var(--ink);letter-spacing:-.5px}
  .address{
    position:absolute;left:38px;top:98px;font-size:12px;line-height:1.4;color:var(--ink);
  }
  .person{position:absolute;right:30px;top:112px;text-align:right}
  .person-name{color:var(--accent);font-weight:600;font-size:15px}
  .person-title{font-size:15px;color:var(--ink)}
  .contacts{
    position:absolute;right:30px;top:168px;text-align:right;font-size:13px;line-height:1.45;
  }
  .contact-line{display:flex;align-items:center;justify-content:flex-end;gap:6px}
  .contact-line svg{width:11px;height:11px;fill:var(--accent)}
  .website{
    position:absolute;left:34px;top:232px;color:var(--light);font-size:11px;letter-spacing:.5px;
    transform:rotate(13deg);transform-origin:left center;
  }
  /* back */
  .card-back{background:var(--band)}
  .back-mark{position:absolute;left:60px;top:50px;width:150px;height:150px;border-radius:50%;background:var(--faint)}
  .back-name{
    position:absolute;right:40px;bottom:34px;color:var(--light);font-weight:800;font-size:46px;letter-spacing:-.5px;
  }
</style>
</head>
<body>
  <section class="card card-front">
    <svg class="swoosh" viewBox="0 0 540 309" preserveAspectRatio="none" aria-hidden="true">
      <path d="M0,150 C170,185 360,245 540,288 L540,309 L0,309 Z" fill="var(--band)"/>
      <path d="M0,138 C170,172 360,232 540,276 L540,288 C360,245 170,185 0,150 Z" fill="var(--accent)"/>
      <path d="M0,200 C190,230 380,280 540,300 L540,309 L0,309 Z" fill="var(--band-dark)"/>
    </svg>
    <div class="brand">
      <span class="brand-mark"></span>
      <span class="brand-name">Nubiro</span>
    </div>
    <p class="address">214, 9th Floor,<br>Harbour Lane<br>VIC</p>
    <div class="person">
      <p class="person-name">Mara Lindqvist</p>
      <p class="person-title">Consultant</p>
    </div>
    <div class="contacts">
      <p class="contact-line">030 555 0142
        <svg viewBox="0 0 24 24"><path d="M6.6 10.8a15 15 0 0 0 6.6 6.6l2.2-2.2a1 1 0 0 1 1-.25 11.4 11.4 0 0 0 3.6.57 1 1 0 0 1 1 1V20a1 1 0 0 1-1 1A17 17 0 0 1 3 4a1 1 0 0 1 1-1h3.5a1 1 0 0 1 1 1c0 1.25.2 2.45.57 3.6a1 1 0 0 1-.25 1z"/></svg></p>
      <p class="contact-line">030 555 0142
        <svg viewBox="0 0 24 24"><rect x="7" y="2" width="10" height="20" rx="2"/></svg></p>
      <p class="contact-line">hi@nubiro.com
        <svg viewBox="0 0 24 24"><path d="M2 5h20v14H2z M2 5l10 8 10-8" stroke="#fff" stroke-width="1.5"/></svg></p>
    </div>
    <p class="website">www.nubiroconsult.com</p>
  </section>

  <section class="card card-back">
    <span class="back-mark"></span>
    <p class="back-name">Nubiro</p>
  </section>
</body>
</html>
```